Company or website name
- www.pmrtechworks.net Harbor Value Systems DBA PMRTechworks
- Links to the website
- www.pmrtechworks.net
- Describe your company and organization and target audience
- We are targeting business customers- small to medium size. The ideal client will have the need fo PC's laptops servers wiring Managed services security cameras etc.
- The design should have the following
- CLEAN design, no humor with a call to action toward our product and services.  Zantrix PC laptop and server products Video surveillance systems Point of sale systems Ledgerwise Assistance Warranty service Managed services Data protection and backup Network security Wiring
- Other Facts

```html
<!DOCTYPE html>
<html lang="en">
<head>
<meta charset="utf-8">
<title>PMRTechworks Trifold Brochure</title>
<link rel="stylesheet" href="https://fonts.googleapis.com/css2?family=Montserrat:wght@400;600;700;800&family=Open+Sans:ital,wght@0,400;0,700;1,400&display=swap">
<style>
  :root{
    --navy:#1d3573;
    --navy-deep:#14265a;
    --royal:#0f5aa6;
    --sky:#2aa8e0;
    --callout:#4f8fd0;
    --paper:#eeeeee;
    --cream:#f4eee5;
    --ink:#2b2f3a;
    --muted:#7d8088;
    --backdrop:#d6d6d6;
    --white:#ffffff;
  }
  *{box-sizing:border-box;margin:0;padding:0}
  html,body{width:1200px;height:906px;overflow:hidden}
  body{background:var(--backdrop);font-family:"Open Sans",Arial,sans-serif;color:var(--ink)}
  .brochure{position:absolute;left:40px;top:40px;width:1120px;height:826px;display:grid;grid-template-columns:repeat(3,1fr);box-shadow:0 6px 24px rgba(0,0,0,.18)}
  .panel{position:relative;overflow:hidden}

  /* Inside flap */
  .benefits{background:var(--paper);padding:34px 30px 0}
  .benefits h2{font-family:"Montserrat",sans-serif;font-weight:700;font-size:17px;line-height:1.25;color:var(--navy);margin-bottom:14px}
  .benefit-list{list-style:disc;padding-left:16px;font-size:11.5px;line-height:1.45}
  .benefit-list li{margin-bottom:3px}
  .benefit-list strong{color:var(--navy-deep)}
  .callout{background:var(--callout);color:var(--white);font-style:italic;font-size:11.5px;line-height:1.5;padding:12px 14px;margin:12px 0 14px}
  .benefits h3{font-family:"Montserrat",sans-serif;font-weight:600;font-size:15px;color:var(--navy);margin:18px 0 12px}
  .partner-grid{display:grid;grid-template-columns:repeat(3,1fr);gap:14px 10px;align-items:center;justify-items:center}
  .partner{font-family:"Open Sans",sans-serif;font-weight:700;font-size:13px;color:var(--ink);display:flex;align-items:center;gap:6px;white-space:nowrap}
  .partner .dot{width:11px;height:11px;border-radius:50%;background:var(--royal)}
  .partner .sq{width:10px;height:10px;background:var(--sky)}
  .badge{width:78px;height:34px;border-radius:4px;background:#5d84c6}
  .benefits-band{position:absolute;left:0;right:0;bottom:0;height:34px;background:var(--royal)}

  /* Back panel */
  .contact{background:var(--white)}
  .contact svg.bg{position:absolute;inset:0}
  .brand{display:flex;align-items:center;gap:10px;justify-content:center}
  .brand .mark{width:16px;height:16px;border-radius:50%;background:var(--sky)}
  .brand .name{font-family:"Montserrat",sans-serif;font-weight:800;color:var(--navy);font-size:30px}
  .contact .brand{position:absolute;top:160px;left:0;right:0}
  .contact-cta{position:absolute;top:326px;left:30px;right:30px;text-align:center;font-family:"Montserrat",sans-serif;color:var(--white)}
  .contact-cta strong{display:block;font-weight:700;font-size:16px;text-transform:uppercase;letter-spacing:.5px}
  .contact-cta span{display:block;font-size:12px;color:#c9d6f2;margin-top:4px}
  .contact-list{position:absolute;top:396px;left:0;right:0;text-align:center;color:var(--white);list-style:none;font-family:"Montserrat",sans-serif}
  .contact-list li{margin-bottom:22px;font-size:14px;line-height:1.45}
  .contact-list svg{display:block;margin:0 auto 8px}
  .contact-list .company{color:var(--sky);font-weight:600}

  /* Cover */
  .cover{background:var(--cream)}
  .cover .brand{margin-top:80px}
  .headline{font-family:"Montserrat",sans-serif;font-weight:800;font-size:24px;line-height:1.2;color:var(--navy);text-align:center;margin-top:30px;text-transform:uppercase}
  .rule{width:40px;height:3px;background:var(--sky);margin:14px auto 0}
  .tagline{font-family:"Montserrat",sans-serif;font-size:12.5px;color:var(--muted);text-align:center;line-height:1.5;margin-top:10px}
  .services{margin:16px 28px 0}
  .services h4{font-family:"Montserrat",sans-serif;font-weight:700;font-size:12px;color:var(--navy);text-transform:uppercase;letter-spacing:.6px;text-align:center;margin-bottom:8px}
  .service-list{list-style:none;display:grid;grid-template-columns:1fr 1fr;gap:4px 12px;font-size:11px;line-height:1.35;color:var(--ink)}
  .service-list li{display:flex;align-items:center;gap:6px}
  .service-list li::before{content:"";flex:none;width:6px;height:6px;border-radius:50%;background:var(--sky)}
  .service-list .wide{grid-column:1 / -1}
  .cover-photo{position:absolute;left:0;right:0;bottom:0;height:372px;background:linear-gradient(160deg,#efe6da 0%,#d9c8b3 45%,#9aa4bf 100%)}
  .cover-url{position:absolute;left:20px;bottom:18px;font-family:"Montserrat",sans-serif;font-weight:600;font-size:12px;color:var(--navy-deep)}
</style>
</head>
<body>
<main class="brochure">

  <section class="panel benefits">
    <h2>Here's how you'll benefit from PMRTechworks and our business solutions:</h2>
    <ul class="benefit-list">
      <li><strong>Never go without IT support again</strong> - We're here for you night and day.</li>
      <li><strong>Save money on products</strong> - We use only COMMERCIAL GRADE products that provide extended life and lower down time.</li>
      <li><strong>Maximize efficiency on the road</strong> - We offer both on site and remote support.</li>
      <li><strong>Benefit from proactive IT solutions</strong> - Our managed services platform identifies and corrects problems before they affect your business.</li>
    </ul>
    <p class="callout">PMRTechworks partners with you and your team to help you reach your business goals. We value long-term relationships with our clients and will work closely with your business to ensure that you have the resources you need to be successful.</p>
    <ul class="benefit-list">
      <li>Our professionals take the time to understand your IT needs and business objectives.</li>
      <li>Our company offers a variety of managed IT service options so you can find a plan that works for your unique business.</li>
      <li>Our experts train your staff on new technologies and provide the support you need to keep your IT up and running.</li>
    </ul>
    <h3>Partners &amp; Certifications</h3>
    <div class="partner-grid">
      <span class="partner">Norvale Partner</span>
      <span class="badge" role="img" aria-label="Small business specialist certification badge"></span>
      <span class="partner">Keepline</span>
      <span class="partner"><span class="dot"></span>Ledgerwise</span>
      <span class="partner">Printaro</span>
      <span class="partner">Zantrix</span>
      <span class="partner">Paxmore</span>
      <span class="partner"><span class="sq"></span>Veyra</span>
      <span class="partner"><span class="sq"></span>Stonemark</span>
    </div>
    <div class="benefits-band"></div>
  </section>

  <section class="panel contact">
    <svg class="bg" width="373" height="826" viewBox="0 0 373 826" aria-hidden="true">
      <defs>
        <linearGradient id="navyFade" x1="0" y1="0" x2="0" y2="1">
          <stop offset="0" stop-color="#25418a"/>
          <stop offset="1" stop-color="#14265a"/>
        </linearGradient>
      </defs>
      <path d="M0 0H373V70Q190 110 0 80Z" fill="#1d3573"/>
      <path d="M0 310Q180 250 373 285V826H0Z" fill="url(#navyFade)"/>
    </svg>
    <div class="brand"><span class="mark"></span><span class="name">PMRTechworks</span></div>
    <div class="contact-cta">
      <strong>Call today for a free IT assessment</strong>
      <span>Find the right plan for your business</span>
    </div>
    <ul class="contact-list">
      <li>
        <svg width="22" height="22" viewBox="0 0 24 24" aria-hidden="true"><circle cx="12" cy="12" r="12" fill="#fff"/><path d="M12 5a4.5 4.5 0 0 0-4.5 4.5C7.5 13 12 19 12 19s4.5-6 4.5-9.5A4.5 4.5 0 0 0 12 5zm0 6.2a1.7 1.7 0 1 1 0-3.4 1.7 1.7 0 0 1 0 3.4z" fill="#1d3573"/></svg>
        <span class="company">Harbor Value Systems TSS Inc.</span><br>4120 Lake Street<br>Eastbrook (Marlow), NY 14031
      </li>
      <li>
        <svg width="22" height="22" viewBox="0 0 24 24" aria-hidden="true"><circle cx="12" cy="12" r="12" fill="#fff"/><path d="M8.6 6.5l1.9-.4 1.1 2.8-1.3 1a7 7 0 0 0 3.8 3.8l1-1.3 2.8 1.1-.4 1.9c-.2.7-.8 1.1-1.5 1A10 10 0 0 1 7.6 8c-.1-.7.3-1.3 1-1.5z" fill="#1d3573"/></svg>
        716-555-0148
      </li>
      <li>
        <svg width="22" height="22" viewBox="0 0 24 24" aria-hidden="true"><circle cx="12" cy="12" r="12" fill="#fff"/><rect x="6" y="8" width="12" height="8" rx="1" fill="#1d3573"/><path d="M6.5 8.5L12 12.5l5.5-4" stroke="#fff" stroke-width="1.2" fill="none"/></svg>
        help@pmrtechworks.net
      </li>
      <li>
        <svg width="22" height="22" viewBox="0 0 24 24" aria-hidden="true"><circle cx="12" cy="12" r="12" fill="#fff"/><circle cx="12" cy="12" r="6" fill="none" stroke="#1d3573" stroke-width="1.4"/><path d="M6 12h12M12 6c-2.5 3-2.5 9 0 12M12 6c2.5 3 2.5 9 0 12" stroke="#1d3573" stroke-width="1.2" fill="none"/></svg>
        www.pmrtechworks.net
      </li>
    </ul>
  </section>

  <section class="panel cover">
    <div class="brand"><span class="mark"></span><span class="name">PMRTechworks</span></div>
    <h1 class="headline">We make your<br>technology work</h1>
    <div class="rule"></div>
    <p class="tagline">Dependable IT Solutions and Computer Support<br>for Homes and Businesses since 1985</p>
    <div class="services">
      <h4>Products &amp; Services</h4>
      <ul class="service-list">
        <li class="wide">Zantrix PC, laptop and server products</li>
        <li>Video surveillance systems</li>
        <li>Point of sale systems</li>
        <li>Ledgerwise assistance</li>
        <li>Warranty service</li>
        <li>Managed services</li>
        <li>Data protection &amp; backup</li>
        <li>Network security</li>
        <li>Wiring</li>
      </ul>
    </div>
    <div class="cover-photo" role="img" aria-label="Photo of a smiling person working on a laptop in a bright room"></div>
    <span class="cover-url">www.pmrtechworks.net</span>
  </section>

</main>
</body>
</html>
```